TILLvanta (www.tillvanta.example) needs exciting professional Business Cards

TILLvanta is an exciting new start-up targeting innovative ways to engage with retail customers at the point of sale.
Our Vision
Through applying new thinking to an old business we are reinventing selected segments of the Australian retail messaging industry, generating significant value for our customers, our suppliers, and our owners.
We operate with integrity, agility, and intelligence to doing things smarter, faster and more efficiently.
We bring deep industry expertise, deep relationships with customers and suppliers, and a will to see the old ways give way to smarter ways – this is why we win.
From this economically sustainable platform, we will examine the disruption of other market segments by further leveraging the elements that make us successful.
Our Values
With our clients, with our suppliers, with our staff, and with our owners:
# We Partner – We align the interest of all stakeholders by striving to ensure everything we do is mutually beneficial and commercially sustainable in the long term. We are clear with all our stakeholders about what our expectations are of them, and we seek clarity from them in their expectations of us.
# We Innovate – In the segments we choose to compete in, we bring fresh ideas, new business processes, the right relationships, and the right technology to ensure the supply chain is nimble, competitive, and reliable.
# We are Accountable – We say what we will do, and then do what we say.
# We Perform – We use our skills, relationships, and reputation to deliver value to our customers, suppliers, and owners.
Initially we are building our business from low-tech through printing promotional offers and retailer messages on ATM and EFTPOS receipts, but as soon as cash flow supports it we will be engaging in high-tech real-time targeted offers to the specific consumer.
I'd like the cards to reflect our values.
Please check out the web site we have just launched - it is pretty basic but it has only been up a week. We intend to sharpen it over the coming weeks, but you'll get the idea of what our core messages are.
I have recently sourced a logo from MarkForge, and have attached the source files for use.
Personal information to include:
Name: FirstName Surname
Title: Managing Director
email: first.surname@tillvanta.example
Mobile: +61-427-318-654
Generic Co Details to include:
Web: www.tillvanta.example
email: tillvanta@tillvanta.example
Fax: +61-8-7394-2816
Offices & Agents: Sydney, Melbourne, Brisbane, Adelaide, Perth
Byline: Innovation . Integrity . Service
Target Market(s)
Our customers are large corporations that have professional Point Of Sale marketing experts looking for a supplier with an edge over others in a crowded market. The buyer of our product and services is ultimately a communications expert.
They want to see distinctive competence, and an agility of thinking that will make them money through driving more consumer spending.
Industry/Entity Type
Retail
Look and feel
Each slider illustrates characteristics of the customer's brand and the style your logo design should communicate.

```html
<!DOCTYPE html>
<html lang="en">
<head>
<meta charset="utf-8">
<title>TILLvanta Business Cards</title>
<link rel="stylesheet" href="https://fonts.googleapis.com/css2?family=Arimo:wght@400;700&display=swap">
<style>
  :root {
    --backdrop: #1e1e1e;
    --brand-blue: #1873b6;
    --band-blue-light: #2a9ad8;
    --band-blue-dark: #0f6fb3;
    --card-white: #ecedee;
    --text-grey: #7c7e80;
  }
  * { box-sizing: border-box; margin: 0; padding: 0; }
  html, body {
    width: 1200px; height: 896px; overflow: hidden;
    background: var(--backdrop);
    font-family: "Arimo", Arial, sans-serif;
  }
  .stage { position: relative; width: 1200px; height: 896px; }

  .card {
    position: absolute; left: 353px; width: 485px; height: 268px;
    background: var(--card-white);
    overflow: hidden;
  }
  .card--front { top: 165px; }
  .card--back { top: 472px; }

  /* Front */
  .band {
    position: absolute; left: 0; width: 100%;
    background: linear-gradient(135deg, var(--band-blue-light), var(--band-blue-dark));
  }
  .band--top { top: 0; height: 83px; }
  .band--bottom { top: 187px; height: 81px; }

  .wordmark {
    position: absolute; color: var(--brand-blue);
    font-weight: 700; text-transform: uppercase;
    letter-spacing: 1px; line-height: 1;
  }
  .card--front .wordmark { left: 64px; top: 102px; font-size: 44px; }
  .tagline {
    position: absolute; left: 65px; top: 159px;
    font-size: 15px; letter-spacing: 1.1px; color: var(--brand-blue);
  }

  /* Back */
  .card--back .wordmark { right: 115px; top: 44px; font-size: 38px; }
  .details {
    position: absolute; right: 115px; text-align: right;
    color: var(--text-grey); font-size: 12.5px; line-height: 15px;
  }
  .person { top: 132px; }
  .person__name { font-size: 18px; line-height: 20px; letter-spacing: 0.3px; }
  .person__title { color: var(--brand-blue); font-size: 13px; line-height: 17px; }
  .person__direct { margin-top: 6px; }
  .label { color: var(--brand-blue); margin-right: 4px; }
  .value + .label { margin-left: 8px; }
  .rule {
    position: absolute; left: 0; top: 195px; width: 370px; height: 1px;
    background: var(--brand-blue);
  }
  .company { top: 206px; }
  .web-brand { color: var(--brand-blue); }
</style>
</head>
<body>
<main class="stage">

  <section class="card card--front" aria-label="Business card front">
    <div class="band band--top"></div>
    <div class="band band--bottom"></div>
    <div class="wordmark">TILLvanta</div>
    <p class="tagline">Innovation | Integrity | Service</p>
  </section>

  <section class="card card--back" aria-label="Business card back">
    <div class="wordmark">TILLvanta</div>

    <div class="details person">
      <p class="person__name">FIRSTNAME SURNAME</p>
      <p class="person__title">Managing Director</p>
      <p class="person__direct">
        <span class="label">m</span><span class="value">+61-427-318-654</span>
        <span class="label">e</span><span class="value">first.surname@tillvanta.example</span>
      </p>
    </div>

    <div class="rule"></div>

    <div class="details company">
      <p>
        <span class="label">f</span><span class="value">+61-8-7394-2816</span>
        <span class="label">e</span><span class="value">tillvanta@tillvanta.example</span>
      </p>
      <p>Sydney, Melbourne, Brisbane, Adelaide, Perth</p>
      <p>www.<span class="web-brand">tillvanta</span>.example</p>
    </div>
  </section>

</main>
</body>
</html>
```